Screenshot Design for Bolt Ware Shop for business application

I will need 5 screenshots of my application "Slidecraft Hub" for the peview page for the Zephyr Ware Shop.

Screenshot requirements are:
One of the following sizes:
2560 x 1600 pixels
2880 x 1800 pixel

I will provide the following resources. Please feel free to take what you think is the best for the preview (any picture, logo, text line of all the files here). At the end, you only need 5 pictures and 5 text points, each for every screenshot.

- Logo files
- PDF preview of the DeckForge slide (please let me know if you need any special slide as PNG, it is too much data to add all PNGs)
- App Screenshot (you can change the picture with one from the pdfs)
- Example texts
- Colors: Blue #3083E8, Dark blue #1F1FB5, Yellow #F0C25D

My application offers business DeckForge templates and the screenshots should not only show the application itself, but some preview slides of the DeckForge templates. In case you have any question, please let me know.
Updates

Target Market(s)

Business people

Industry/Entity Type

Business

Font styles to use
Sans Serif

Requirements
Must have
• - One screenshot should show the application screenshot
• - Please use only the following colors: Blue #3083E8, Dark blue #1F1FB5, Yellow #F0C25D
• - Please look at other pictures of the Zephyr Wareshop (https://tunevault.example.com/us/genre/zephyr/id57?mt=14) and adapt your design to those
Nice to have
• - The blue as background would be preferred

```html
<!DOCTYPE html>
<html lang="en">
<head>
<meta charset="utf-8">
<title>Slidecraft Hub – Charts</title>
<link href="https://fonts.googleapis.com/css2?family=Montserrat:wght@400;700&family=Roboto:wght@400;500&display=swap" rel="stylesheet">
<style>
  :root{
    --blue:#3083E8;
    --white:#ffffff;
    --chart:#9a6b60;
    --chart-light:#c8aaa2;
    --chart-mid:#b18a80;
    --chart-dark:#7f6a66;
    --bar-top:#e9e9e9;
    --bar-edge:#cfcfcf;
    --ink:#3a2a26;
  }
  *{margin:0;padding:0;box-sizing:border-box}
  html,body{width:1200px;height:750px;overflow:hidden}
  body{background:var(--blue);font-family:"Roboto",Arial,sans-serif;position:relative}
  .headline{position:absolute;left:78px;top:100px;color:var(--white);font-family:"Montserrat",Arial,sans-serif;font-weight:700;font-size:50px;line-height:60px;letter-spacing:-.5px}
  .subline{position:absolute;left:78px;top:395px;color:var(--white);font-size:33px;line-height:41px}
  .window{position:absolute;left:430px;width:790px;background:var(--white);overflow:hidden;box-shadow:0 -2px 6px rgba(0,0,0,.25);border-top-left-radius:4px}
  .titlebar{height:24px;background:var(--bar-top);border-bottom:1px solid var(--bar-edge);display:flex;align-items:center;padding-left:10px;gap:6px}
  .dot{width:9px;height:9px;border-radius:50%}
  .dot.close{background:#fc605c}.dot.min{background:#fdbc40}.dot.max{background:#34c84a}
  .nav{width:18px;height:15px;border:1px solid var(--bar-edge);background:#f6f6f6;border-radius:3px}
  .nav:first-of-type{margin-left:14px}
  .nav.sidebar{width:22px;margin-left:6px}
  .window svg{display:block}
  .w-pie{top:80px;height:120px}
  .w-columns{top:180px;height:100px}
  .w-rows{top:268px;height:140px}
  .w-lines{top:398px;height:255px}
  svg text{font-family:"Montserrat",Arial,sans-serif}
</style>
</head>
<body>
  <h1 class="headline">Everything<br>you need for<br>a business<br>presentation</h1>
  <p class="subline">Wide range of bar,<br>line and other graphs</p>

  <section class="window w-pie">
    <div class="titlebar"><span class="dot close"></span><span class="dot min"></span><span class="dot max"></span><span class="nav"></span><span class="nav"></span><span class="nav sidebar"></span></div>
    <svg width="790" height="96" viewBox="0 0 790 96">
      <g transform="translate(180,120)">
        <path d="M-95,0 A95,95 0 0 1 -67,-67 L-32,-32 A45,45 0 0 0 -45,0Z" fill="var(--chart-dark)"/>
        <path d="M-67,-67 A95,95 0 0 1 0,-95 L0,-45 A45,45 0 0 0 -32,-32Z" fill="var(--chart-light)"/>
        <path d="M0,-95 A95,95 0 0 1 95,0 L45,0 A45,45 0 0 0 0,-45Z" fill="var(--chart-mid)"/>
        <text x="-28" y="-66" fill="#fff" font-size="12" text-anchor="middle">Text</text>
        <text x="-28" y="-52" fill="#fff" font-size="11" text-anchor="middle">9%</text>
        <text x="-62" y="-40" fill="#fff" font-size="12" text-anchor="middle">Text</text>
      </g>
      <g transform="translate(460,120)">
        <path d="M-95,0 A95,95 0 0 1 -67,-67 L-32,-32 A45,45 0 0 0 -45,0Z" fill="var(--chart-dark)"/>
        <path d="M-67,-67 A95,95 0 0 1 0,-95 L0,-45 A45,45 0 0 0 -32,-32Z" fill="var(--chart-light)"/>
        <path d="M0,-95 A95,95 0 0 1 95,0 L45,0 A45,45 0 0 0 0,-45Z" fill="var(--chart)"/>
        <text x="-28" y="-66" fill="#fff" font-size="12" text-anchor="middle">Text</text>
        <text x="-28" y="-52" fill="#fff" font-size="11" text-anchor="middle">9%</text>
        <text x="-62" y="-40" fill="#fff" font-size="12" text-anchor="middle">Text</text>
      </g>
      <g transform="translate(740,120)">
        <path d="M-95,0 A95,95 0 0 1 -67,-67 L-32,-32 A45,45 0 0 0 -45,0Z" fill="var(--chart-dark)"/>
        <path d="M-67,-67 A95,95 0 0 1 0,-95 L0,-45 A45,45 0 0 0 -32,-32Z" fill="var(--chart-light)"/>
      </g>
    </svg>
  </section>

  <section class="window w-columns">
    <div class="titlebar"><span class="dot close"></span><span class="dot min"></span><span class="dot max"></span><span class="nav"></span><span class="nav"></span><span class="nav sidebar"></span></div>
    <svg width="790" height="76" viewBox="0 0 790 76" font-size="13" fill="var(--ink)">
      <g fill="var(--chart)">
        <rect x="112" y="56" width="22" height="20"/><rect x="152" y="53" width="22" height="23"/>
        <rect x="194" y="50" width="22" height="26"/><rect x="235" y="56" width="22" height="20"/>
        <rect x="276" y="60" width="22" height="16"/><rect x="317" y="64" width="22" height="12"/>
        <rect x="457" y="60" width="22" height="16"/><rect x="499" y="28" width="22" height="48"/>
        <rect x="541" y="34" width="22" height="42"/><rect x="583" y="30" width="22" height="46"/>
        <rect x="728" y="8" width="70" height="14"/><rect x="728" y="38" width="70" height="14"/>
      </g>
      <text x="112" y="48">23</text><text x="152" y="45">25</text><text x="194" y="42">28</text>
      <text x="235" y="48">23</text><text x="276" y="52">21</text><text x="317" y="56">19</text>
      <text x="418" y="70">12</text><text x="457" y="52">22</text><text x="499" y="20">34</text>
      <text x="541" y="26">32</text><text x="583" y="22">33</text><text x="626" y="70">12</text>
      <text x="680" y="19">Text</text><text x="680" y="49">Text</text>
    </svg>
  </section>

  <section class="window w-rows">
    <div class="titlebar"><span class="dot close"></span><span class="dot min"></span><span class="dot max"></span><span class="nav"></span><span class="nav"></span><span class="nav sidebar"></span></div>
    <svg width="790" height="116" viewBox="0 0 790 116" font-size="14" fill="var(--ink)">
      <rect x="155" y="8" width="28" height="80" fill="var(--chart)"/>
      <text transform="translate(175,72) rotate(-90)" fill="#fff" font-size="15" letter-spacing="1">Title</text>
      <rect x="158" y="96" width="28" height="20" fill="var(--chart)"/>
      <line x1="240" y1="8" x2="240" y2="116" stroke="#ddd"/>
      <rect x="245" y="12" width="370" height="18" fill="var(--chart)"/>
      <rect x="245" y="42" width="395" height="18" fill="var(--chart)"/>
      <text x="192" y="27">Text</text><text x="192" y="57">Text</text>
      <text x="628" y="27">13</text><text x="652" y="57">14</text>
      <g font-size="13">
        <text x="690" y="16">Lorem ipsum</text><text x="690" y="32">consetetur s</text>
        <text x="690" y="48">nonumy eirm</text><text x="690" y="64">labore et do</text>
        <text x="690" y="114">Lorem ipsum</text>
      </g>
      <rect x="245" y="110" width="320" height="6" fill="var(--chart)"/>
    </svg>
  </section>

  <section class="window w-lines">
    <div class="titlebar"><span class="dot close"></span><span class="dot min"></span><span class="dot max"></span><span class="nav"></span><span class="nav"></span><span class="nav sidebar"></span></div>
    <svg width="790" height="231" viewBox="0 0 790 231" font-size="9" fill="var(--ink)">
      <rect x="75" y="14" width="400" height="14" fill="var(--chart)"/>
      <text x="275" y="24" fill="#fff" text-anchor="middle" letter-spacing="3">Title</text>
      <text x="85" y="38">Text</text>
      <polyline points="130,128 175,115 220,78 265,74 310,80 355,76 400,84 445,80" fill="none" stroke="var(--chart)" stroke-width="2"/>
      <g fill="var(--chart)">
        <circle cx="130" cy="128" r="2.5"/><circle cx="175" cy="115" r="2.5"/><circle cx="220" cy="78" r="2.5"/>
        <circle cx="265" cy="74" r="2.5"/><circle cx="310" cy="80" r="2.5"/><circle cx="355" cy="76" r="2.5"/>
        <circle cx="400" cy="84" r="2.5"/><circle cx="445" cy="80" r="2.5"/>
      </g>
      <text x="120" y="122">15</text><text x="167" y="108">27</text><text x="212" y="70">56</text>
      <text x="257" y="66">59</text><text x="302" y="72">55</text><text x="347" y="68">58</text>
      <text x="392" y="76">52</text><text x="437" y="72">54</text>
      <line x1="110" y1="148" x2="470" y2="148" stroke="#ccc"/>
      <g text-anchor="middle">
        <text x="130" y="160">Text</text><text x="175" y="160">Text</text><text x="220" y="160">Text</text>
        <text x="265" y="160">Text</text><text x="310" y="160">Text</text><text x="355" y="160">Text</text>
        <text x="400" y="160">Text</text><text x="445" y="160">Text</text>
        <text x="290" y="176">Lorem ipsum dolor sit amet, consetetur sadipscing</text>
        <text x="290" y="186">elitr, sed diam nonumy eirmod tempor invidunt ut</text>
        <text x="290" y="196">labore et dolore magna aliquyam erat, sed diam</text>
      </g>
      <rect x="565" y="14" width="240" height="14" fill="var(--chart)"/>
      <text x="720" y="24" fill="#fff" letter-spacing="3">Title</text>
      <text x="575" y="38">Text</text>
      <polyline points="605,90 650,78 695,110 740,74 785,90" fill="none" stroke="var(--chart)" stroke-width="2"/>
      <g fill="var(--chart)">
        <circle cx="605" cy="90" r="2.5"/><circle cx="650" cy="78" r="2.5"/><circle cx="695" cy="110" r="2.5"/><circle cx="740" cy="74" r="2.5"/>
      </g>
      <text x="595" y="84">55</text><text x="642" y="70">58</text><text x="688" y="124">52</text><text x="732" y="66">59</text>
      <line x1="580" y1="148" x2="790" y2="148" stroke="#ccc"/>
      <g text-anchor="middle">
        <text x="605" y="160">Text</text><text x="650" y="160">Text</text><text x="695" y="160">Text</text><text x="740" y="160">Text</text><text x="785" y="160">Text</text>
      </g>
      <text x="590" y="176">Lorem ipsum dolor sit amet,</text>
      <text x="590" y="186">elitr, sed diam nonumy eirm</text>
      <text x="590" y="196">labore et dolore magna aliq</text>
    </svg>
  </section>
</body>
</html>
```